Calendar Dates Only

Need monthly 2018 calendar showing Australian holidays. Need 2 versions 1 black and white and one with some colour. Also need calendar with week starting on Mondays and also on Sundays. Prefer Indesign versions so text can be changed if necessary. Dates only required which would be A4 landscape format. May also need portrait format.

Colors

```html
<!DOCTYPE html>
<html lang="en">
<head>
<meta charset="utf-8">
<title>January 2018</title>
<link href="https://fonts.googleapis.com/css2?family=Arimo:wght@400;700&display=swap" rel="stylesheet">
<style>
  :root {
    --ink: #000000;
    --paper: #ffffff;
    --date-blue: #0e4a6e;
    --holiday-red: #a3003c;
    --rule: #000000;
  }
  * { box-sizing: border-box; margin: 0; padding: 0; }
  html, body { width: 1200px; height: 848px; overflow: hidden; background: var(--paper); }
  body { position: relative; font-family: "Arimo", Arial, sans-serif; color: var(--ink); }

  .month-title {
    position: absolute; top: 58px; left: 0; width: 1200px;
    text-align: center; font-size: 37px; font-weight: 400; letter-spacing: 0.2px;
  }

  .calendar {
    position: absolute; left: 63px; top: 120px; width: 1074px;
  }
  .weekdays {
    display: grid; grid-template-columns: repeat(7, 1fr);
    height: 20px; background: var(--ink);
  }
  .weekday {
    color: var(--paper); font-weight: 700; font-size: 15px;
    text-align: center; line-height: 20px;
  }
  .days {
    display: grid; grid-template-columns: repeat(7, 1fr); grid-auto-rows: 119.6px;
    border-left: 1px solid var(--rule);
  }
  .day {
    position: relative;
    border-right: 1px solid var(--rule); border-bottom: 1px solid var(--rule);
  }
  .day-number {
    position: absolute; top: 44px; left: 0; right: 0; text-align: center;
    font-size: 17px; font-weight: 700; color: var(--date-blue);
  }
  .day-note {
    position: absolute; top: 91px; left: 0; right: 0; text-align: center;
    font-size: 11px; letter-spacing: -0.3px;
  }
  .day-note.holiday { color: var(--holiday-red); }
  .moon {
    position: absolute; top: 17px; right: 13px; width: 18px; height: 18px;
  }
</style>
</head>
<body>
  <h1 class="month-title">JANUARY 2018</h1>

  <div class="calendar">
    <div class="weekdays">
      <div class="weekday">Sun</div><div class="weekday">Mon</div><div class="weekday">Tue</div>
      <div class="weekday">Wed</div><div class="weekday">Thu</div><div class="weekday">Fri</div>
      <div class="weekday">Sat</div>
    </div>

    <div class="days">
      <div class="day"></div>
      <div class="day"><span class="day-number">1</span><span class="day-note holiday">New Year's Day</span></div>
      <div class="day"><span class="day-number">2</span>
        <svg class="moon" viewBox="0 0 18 18" aria-label="Full moon"><circle cx="9" cy="9" r="7.5" fill="none" stroke="#0e4a6e" stroke-width="1.5"/></svg>
      </div>
      <div class="day"><span class="day-number">3</span></div>
      <div class="day"><span class="day-number">4</span></div>
      <div class="day"><span class="day-number">5</span></div>
      <div class="day"><span class="day-number">6</span></div>

      <div class="day"><span class="day-number">7</span></div>
      <div class="day"><span class="day-number">8</span></div>
      <div class="day"><span class="day-number">9</span>
        <svg class="moon" viewBox="0 0 18 18" aria-label="Last quarter"><circle cx="9" cy="9" r="7.5" fill="none" stroke="#0e4a6e" stroke-width="1.5"/><path d="M9 1.5 A7.5 7.5 0 0 0 9 16.5 Z" fill="#0e4a6e"/></svg>
      </div>
      <div class="day"><span class="day-number">10</span></div>
      <div class="day"><span class="day-number">11</span></div>
      <div class="day"><span class="day-number">12</span></div>
      <div class="day"><span class="day-number">13</span></div>

      <div class="day"><span class="day-number">14</span></div>
      <div class="day"><span class="day-number">15</span></div>
      <div class="day"><span class="day-number">16</span></div>
      <div class="day"><span class="day-number">17</span>
        <svg class="moon" viewBox="0 0 18 18" aria-label="New moon"><circle cx="9" cy="9" r="8.2" fill="#0e4a6e"/></svg>
      </div>
      <div class="day"><span class="day-number">18</span></div>
      <div class="day"><span class="day-number">19</span></div>
      <div class="day"><span class="day-number">20</span></div>

      <div class="day"><span class="day-number">21</span><span class="day-note">World Religion Day</span></div>
      <div class="day"><span class="day-number">22</span></div>
      <div class="day"><span class="day-number">23</span></div>
      <div class="day"><span class="day-number">24</span></div>
      <div class="day"><span class="day-number">25</span>
        <svg class="moon" viewBox="0 0 18 18" aria-label="First quarter"><circle cx="9" cy="9" r="7.5" fill="none" stroke="#0e4a6e" stroke-width="1.5"/><path d="M9 1.5 A7.5 7.5 0 0 0 9 16.5 Z" fill="#0e4a6e"/></svg>
      </div>
      <div class="day"><span class="day-number">26</span><span class="day-note holiday">Australia Day</span></div>
      <div class="day"><span class="day-number">27</span></div>

      <div class="day"><span class="day-number">28</span></div>
      <div class="day"><span class="day-number">29</span></div>
      <div class="day"><span class="day-number">30</span></div>
      <div class="day"><span class="day-number">31</span></div>
      <div class="day"></div>
      <div class="day"></div>
      <div class="day"></div>
    </div>
  </div>
</body>
</html>
```